Greeting Cards for all Occasions

We are a large church and are sending cards all the time for different occasions. We'd like to have 5 different cards designed that fit with our brand guidelines and logo (Attached). We'd like to have designs for the following 5x7 cards. Each title should be featured on the front, and the inside should be blank, with the back should feature the contact info below. Appropriate photos from Unsplash are welcomed.

1. Happy Birthday
2. Get Well Soon
3. Praying for You
4. Happy Anniversary
5. Thank You

Contact info to include on the back:
Millbrook Chapel
4817 Tamsin Avenue, Alder Springs, OR 97321
www.MillbrookChapel.com I 541-418-5502

```html
<!DOCTYPE html>
<html lang="en">
<head>
<meta charset="utf-8">
<title>Millbrook Chapel Greeting Cards</title>
<link href="https://fonts.googleapis.com/css2?family=Montserrat:wght@600;800&display=swap" rel="stylesheet">
<style>
  :root {
    --stage: #1e1e1e;
    --white: #ffffff;
    --ink: #000000;
    --back-paper: #ffffff;
  }
  * { box-sizing: border-box; margin: 0; padding: 0; }
  html, body { width: 1200px; height: 1110px; overflow: hidden; background: var(--stage); }
  body { position: relative; font-family: "Montserrat", Arial, sans-serif; }

  .card { position: absolute; width: 370px; height: 518px; overflow: hidden; }
  .card--birthday    { left: 24px;  top: 25px; }
  .card--get-well    { left: 414px; top: 25px; }
  .card--anniversary { left: 804px; top: 25px; }
  .card--praying     { left: 24px;  top: 566px; }
  .card--thanks      { left: 413px; top: 566px; width: 372px; }
  .card--back        { left: 804px; top: 566px; background: var(--back-paper); }

  .card__photo { position: absolute; inset: 0; }
  .card--birthday .card__photo {
    background: radial-gradient(ellipse at 52% 50%, #8a6a52 0%, #4a3a30 30%, #2b231e 70%, #1f1a17 100%);
  }
  .card--get-well .card__photo {
    background:
      radial-gradient(ellipse 42% 32% at 62% 55%, #7a4a2a 0%, #6a4026 60%, transparent 100%),
      linear-gradient(180deg, #e8e5cb 0%, #e2dec0 62%, #d8d3b3 80%, #e0dcc0 100%);
  }
  .card--anniversary .card__photo {
    background:
      radial-gradient(ellipse at 75% 25%, #d9d08a 0%, transparent 45%),
      linear-gradient(180deg, #8c8a52 0%, #6f7440 40%, #7b6c4f 70%, #5d4d3b 100%);
  }
  .card--praying .card__photo {
    background:
      radial-gradient(ellipse 40% 30% at 62% 70%, #a58f7c 0%, transparent 100%),
      linear-gradient(90deg, #6f6a5c 0%, #3c312b 25%, #3a2f29 80%, #5a4a3e 100%);
  }
  .card--thanks .card__photo {
    background:
      radial-gradient(ellipse 35% 22% at 45% 50%, #e6c8b8 0%, transparent 100%),
      linear-gradient(180deg, #d2e0f0 0%, #dfe9f5 50%, #eef3fa 100%);
  }

  .card__frame {
    position: absolute; left: 20px; top: 19px; right: 19px; bottom: 18px;
    border: 4px solid var(--white);
  }
  .card--get-well .card__frame,
  .card--thanks .card__frame { border-color: var(--ink); }

  .card__title {
    position: absolute; left: 44px;
    font-weight: 800; font-size: 50px; line-height: 0.98;
    letter-spacing: 0.5px; text-transform: uppercase; color: var(--white);
  }
  .card--birthday .card__title    { top: 80px; }
  .card--get-well .card__title    { top: 40px; color: var(--ink); }
  .card--anniversary .card__title { top: 232px; }
  .card--anniversary .card__title .small { font-size: 37px; display: block; letter-spacing: 0; }
  .card--praying .card__title     { top: 123px; }
  .card--thanks .card__title      { top: 312px; left: auto; right: 42px; text-align: right; color: var(--ink); }

  .brand {
    position: absolute; left: 46px; bottom: 44px;
    display: flex; align-items: center; gap: 5px;
    font-weight: 600; font-size: 17px; letter-spacing: 2.4px; color: var(--white);
  }
  .brand__dot { width: 13px; height: 13px; border-radius: 50%; background: currentColor; }
  .card--get-well .brand { color: var(--ink); }
  .card--thanks .brand { left: auto; right: 46px; color: var(--ink); }

  .back__name {
    position: absolute; left: 0; right: 0; top: 336px; text-align: center;
    font-weight: 800; font-size: 20px; color: var(--ink);
  }
  .back__contact {
    position: absolute; left: 0; right: 0; top: 397px; text-align: center;
    font-size: 8px; line-height: 9.6px; color: var(--ink); font-weight: 600;
  }
  .back__contact strong { font-weight: 800; }
</style>
</head>
<body>
  <section class="card card--birthday">
    <div class="card__photo" role="img" aria-label="Cupcake with whipped frosting and pomegranate seeds on a dark wooden table"></div>
    <div class="card__frame"></div>
    <h2 class="card__title">Happy<br>Birthday</h2>
    <div class="brand"><span class="brand__dot"></span>millbrook</div>
  </section>

  <section class="card card--get-well">
    <div class="card__photo" role="img" aria-label="Brown teddy bear with a bandage tucked under a cream blanket"></div>
    <div class="card__frame"></div>
    <h2 class="card__title">Get<br>Well<br>Soon</h2>
    <div class="brand"><span class="brand__dot"></span>millbrook</div>
  </section>

  <section class="card card--anniversary">
    <div class="card__photo" role="img" aria-label="Couple holding hands on a sunlit forest path"></div>
    <div class="card__frame"></div>
    <h2 class="card__title">Happy<span class="small">Anniversary</span></h2>
    <div class="brand"><span class="brand__dot"></span>millbrook</div>
  </section>

  <section class="card card--praying">
    <div class="card__photo" role="img" aria-label="Hands folded in prayer over an open Bible"></div>
    <div class="card__frame"></div>
    <h2 class="card__title">Praying<br>For You</h2>
    <div class="brand"><span class="brand__dot"></span>millbrook</div>
  </section>

  <section class="card card--thanks">
    <div class="card__photo" role="img" aria-label="Person in a light blue shirt with hands crossed over the heart"></div>
    <div class="card__frame"></div>
    <h2 class="card__title">Thank<br>You</h2>
    <div class="brand"><span class="brand__dot"></span>millbrook</div>
  </section>

  <section class="card card--back">
    <div class="back__name">Millbrook</div>
    <p class="back__contact">
      <strong>Millbrook Chapel</strong><br>
      4817 Tamsin Avenue, Alder Springs, OR 97321<br>
      541-418-5502<br>
      www.MillbrookChapel.com
    </p>
  </section>
</body>
</html>
```